Criação de Papelaria Profissional para Consultoria de Negócios
A empresa queria:
" Consultoria em planejamento estratégico... marketing... aulas.. palestras.. artigos e livros publicados "

```html
<!DOCTYPE html>
<html lang="pt-BR">
<head>
<meta charset="utf-8">
<title>Envelope – Rafael Monteiro Consultoria</title>
<link rel="stylesheet" href="https://fonts.googleapis.com/css2?family=Cinzel:wght@500&family=Open+Sans:wght@400&display=swap">
<style>
  :root {
    --bg: #ecebe8;
    --charcoal: #2d2d2e;
    --charcoal-dark: #242425;
    --flap: #2a2a2b;
    --paper: #ffffff;
    --accent: #e8541e;
    --ink: #3a3a3c;
    --muted: #9a9a9c;
  }
  * { margin: 0; padding: 0; box-sizing: border-box; }
  html, body { width: 1200px; height: 1200px; overflow: hidden; }
  body { background: var(--bg); position: relative; font-family: "Open Sans", sans-serif; }

  .envelope { position: absolute; inset: 0; }
  .envelope-art { position: absolute; left: 0; top: 0; width: 1200px; height: 1200px; }

  .brand { position: absolute; text-align: center; font-family: "Cinzel", serif; font-weight: 500; }
  .brand-back { left: 197px; top: 545px; width: 444px; color: var(--paper); }
  .brand-front { left: 700px; top: 540px; width: 320px; color: var(--ink); }
  .brand-name { font-size: 26px; letter-spacing: 1px; line-height: 1.1; white-space: nowrap; }
  .brand-back .brand-name { font-size: 22px; }
  .brand-tagline { margin-top: 8px; font-size: 10px; letter-spacing: 6px; text-transform: uppercase; color: var(--ink); }

  .contact { position: absolute; left: 214px; top: 706px; list-style: none; }
  .contact li { display: flex; align-items: center; gap: 10px; margin-bottom: 9px; }
  .contact .icon { width: 18px; height: 18px; border-radius: 50%; background: var(--accent); flex: none; display: flex; align-items: center; justify-content: center; }
  .contact .icon svg { display: block; }
  .contact .lines { font-size: 9px; line-height: 1.35; color: var(--muted); white-space: nowrap; }
</style>
</head>
<body>
  <main class="envelope">
    <svg class="envelope-art" viewBox="0 0 1200 1200" aria-hidden="true">
      <path class="side-flap" d="M197 271 L130 300 Q115 306 115 322 L115 778 Q115 794 130 800 L197 828 Z" fill="var(--flap)"/>
      <path class="top-flap" d="M197 271 L197 207 Q197 192 212 192 L595 192 Q615 192 624 210 L641 271 Z" fill="var(--charcoal-dark)"/>
      <path class="bottom-flap" d="M197 823 L197 910 Q197 924 212 924 L595 924 Q615 924 624 906 L641 823 Z" fill="var(--charcoal-dark)"/>
      <rect class="back-panel" x="197" y="271" width="444" height="552" fill="var(--charcoal)"/>
      <rect class="front-face" x="641" y="271" width="444" height="552" fill="var(--paper)"/>
      <path class="accent-top" d="M410 271 L1085 271 L1085 278 L402 278 Z" fill="var(--accent)"/>
      <path class="highlight-top" d="M300 271 L395 271 L388 276 L300 276 Z" fill="var(--paper)"/>
      <rect class="accent-bottom" x="197" y="812" width="888" height="6" fill="var(--accent)"/>
    </svg>

    <div class="brand brand-back">
      <div class="brand-name">Rafael Monteiro</div>
    </div>

    <div class="brand brand-front">
      <div class="brand-name">Rafael Monteiro</div>
      <div class="brand-tagline">o estrategista</div>
    </div>

    <ul class="contact">
      <li>
        <span class="icon">
          <svg width="10" height="8" viewBox="0 0 10 8"><rect x="0.5" y="0.5" width="9" height="7" fill="none" stroke="#fff"/><path d="M0.5 0.5 L5 4.5 L9.5 0.5" fill="none" stroke="#fff"/></svg>
        </span>
        <span class="lines">contato@monteiroconsult.com.br<br>www.monteiroconsult.com.br</span>
      </li>
      <li>
        <span class="icon">
          <svg width="8" height="10" viewBox="0 0 8 10"><rect x="0.5" y="0.5" width="7" height="9" rx="1.5" fill="none" stroke="#fff"/><circle cx="4" cy="8" r="0.7" fill="#fff"/></svg>
        </span>
        <span class="lines">(21) 9876-5432<br>(21) 3456-7890</span>
      </li>
      <li>
        <span class="icon">
          <svg width="8" height="10" viewBox="0 0 8 10"><path d="M4 9.5 C1 6 0.5 4.5 0.5 3.5 A3.5 3.5 0 0 1 7.5 3.5 C7.5 4.5 7 6 4 9.5 Z" fill="#fff"/><circle cx="4" cy="3.5" r="1.2" fill="#e8541e"/></svg>
        </span>
        <span class="lines">Rua das Palmeiras, 120 - Rio de Janeiro</span>
      </li>
    </ul>
  </main>
</body>
</html>
```